Carpet Cleaning Door Hanger Design Project

please design a door hanger for us. we do carpet cleaning. our company name is Velta Rug Works. our telephone number is 866-402-5719.

please make a special offer coupon.

please add bullets containing the following info-
Professional carpet, hardwood, tile & grout deep steam cleaning.
kid & pet safe.
fast drying.
100% eco friendly / toxin free products.
pet stain/s & odor control.
same day appointments.
clean uniformed employees.
and please put few other catchy lines.

please make a $20.00 of carpet cleaning coupon (restrictions apply).
please make a rooms starting at $59.99 (restrictions apply).

please also put- when you want the best for less call velta rug works.

Target Market(s)

home owners, home renters. new home buyers. new home sellers.

Industry/Entity Type

Home Improvement

Requirements
Must have
• special offer.
• double sided.
• must be a design for a door hanger.
Nice to have
• 100% satisfaction guaranteed bubble.
Should not have
• no website please

```html
<!DOCTYPE html>
<html lang="en">
<head>
<meta charset="utf-8">
<title>Velta Rug Works Door Hanger</title>
<link rel="stylesheet" href="https://fonts.googleapis.com/css2?family=Montserrat:wght@500;700;800&family=Rubik:wght@700;800;900&family=Pacifico&display=swap">
<style>
:root{
  --stage-top:#3a3a3c;
  --stage-bottom:#7f8083;
  --blue-deep:#2f6db5;
  --blue-mid:#4f8ad0;
  --blue-light:#8dbbe6;
  --texture:#c7ddf0;
  --texture-dark:#a9c8e6;
  --hole:#fbf6c0;
  --cut:#e0262c;
  --ink:#1f1f21;
  --white:#ffffff;
  --red:#e61e27;
}
*{margin:0;padding:0;box-sizing:border-box}
html,body{width:1173px;height:1200px;overflow:hidden}
body{position:relative;background:linear-gradient(to bottom,var(--stage-top) 0 922px,var(--stage-bottom) 922px 100%);font-family:"Montserrat",sans-serif}
.hanger{position:absolute;top:98px;width:430px;height:1004px;overflow:hidden;box-shadow:0 2px 6px rgba(0,0,0,.35)}
.hanger--front{left:134px;background:var(--white)}
.hanger--back{left:608px;background:radial-gradient(circle at 30% 20%,var(--texture) 0,var(--texture-dark) 60%,var(--texture) 100%)}
.cutline{position:absolute;left:0;top:0}
.band{position:absolute;left:0;width:100%;background:linear-gradient(to bottom,var(--blue-deep),var(--blue-light) 50%,var(--blue-deep))}
.brand{color:var(--white);font-weight:800;text-align:center;line-height:1;letter-spacing:-1px;text-shadow:0 3px 4px rgba(0,0,0,.35)}
.front-band{top:228px;height:190px;display:flex;align-items:center;justify-content:center}
.front-band .brand{font-size:60px}
.front-texture{position:absolute;top:418px;left:0;width:100%;height:343px;background:var(--texture)}
.photo{position:absolute;top:17px;left:20px;width:390px;height:313px;background:linear-gradient(to bottom,#d9cfc3 0,#cbbfae 55%,#7c7a80 100%)}
.offer{position:absolute;top:761px;left:0;width:100%;height:243px;background:linear-gradient(to bottom,var(--blue-light),var(--blue-mid))}
.offer-script{position:absolute;left:34px;top:-40px;font-family:"Pacifico",cursive;font-size:50px;color:var(--blue-deep);-webkit-text-stroke:1.5px var(--white);transform:rotate(-16deg)}
.offer-price{position:absolute;left:64px;top:0;font-family:"Rubik",sans-serif;font-weight:900;color:var(--red);-webkit-text-stroke:3px var(--white);paint-order:stroke fill;line-height:1;white-space:nowrap}
.offer-price .cur{font-size:90px;vertical-align:top;position:relative;top:58px}
.offer-price .amt{font-size:178px;letter-spacing:-4px}
.offer-line{position:absolute;color:var(--white);white-space:nowrap}
.offer-line--main{top:168px;left:68px;font-size:24px;font-weight:500;letter-spacing:2px}
.offer-line--note{top:198px;right:60px;font-size:13px;font-weight:500}
.menu{position:absolute;left:28px;top:230px;width:374px;border:2px solid var(--ink);font-family:"Rubik",sans-serif}
.menu-head{background:linear-gradient(to bottom,var(--blue-deep),var(--blue-light) 55%,var(--blue-deep));color:var(--white);text-align:center;font-weight:900;font-size:28px;line-height:1;display:flex;flex-direction:column;justify-content:center;text-shadow:0 2px 2px rgba(0,0,0,.3)}
.menu-head small{font-size:15px;font-weight:800;margin-top:3px}
.menu-price{background:var(--white);display:flex;align-items:center;border-top:2px solid var(--ink);border-bottom:2px solid var(--ink);color:var(--ink)}
.amount{font-weight:900;font-size:66px;letter-spacing:-3px;line-height:1;padding-left:10px;width:190px;white-space:nowrap}
.amount sup{font-size:28px;vertical-align:top;position:relative;top:4px;letter-spacing:0}
.amount .small{font-size:40px;letter-spacing:-1px}
.terms{flex:1;text-align:center;font-weight:800;font-size:12.5px;line-height:1.3;padding-right:6px}
.terms b{display:block;font-size:18px;font-weight:800}
.perks{background:var(--white);border-top:2px solid var(--ink);list-style:none;padding:8px 12px;color:var(--ink);font-family:"Montserrat",sans-serif;font-weight:700;font-size:12px;line-height:1.42}
.perks li{display:flex;gap:6px;align-items:flex-start}
.perks svg{flex:none;margin-top:3px}
.back-band{top:684px;height:320px}
.back-brand{position:absolute;top:46px;left:0;width:100%}
.back-brand .brand{font-size:56px}
.phone{position:absolute;top:168px;left:0;width:100%;text-align:center;color:var(--white);font-weight:800;font-size:40px;letter-spacing:-.5px;text-shadow:0 3px 4px rgba(0,0,0,.35)}
.tagline{position:absolute;top:236px;left:0;width:100%;height:56px;background:var(--white);display:flex;align-items:center;justify-content:center;text-align:center;font-weight:800;font-size:15px;line-height:1.25;color:var(--ink)}
</style>
</head>
<body>

<section class="hanger hanger--front">
  <svg class="cutline" width="430" height="228" viewBox="0 0 430 228">
    <line x1="103" y1="0" x2="162" y2="70" stroke="var(--cut)" stroke-width="1.6" stroke-dasharray="6 4"/>
    <circle cx="215" cy="134" r="75" fill="var(--hole)" stroke="var(--cut)" stroke-width="1.6" stroke-dasharray="6 4"/>
  </svg>
  <div class="band front-band"><h1 class="brand">VELTA RUG<br>WORKS</h1></div>
  <div class="front-texture">
    <div class="photo" role="img" aria-label="Technician steam cleaning a carpet with a wand"></div>
  </div>
  <div class="offer">
    <div class="offer-script">Special</div>
    <div class="offer-price"><span class="cur">$</span><span class="amt">98</span></div>
    <p class="offer-line offer-line--main">Only... ANY 3 AREAS</p>
    <p class="offer-line offer-line--note">Up to 350 “cleanable” sq feet</p>
  </div>
</section>

<section class="hanger hanger--back">
  <svg class="cutline" width="430" height="228" viewBox="0 0 430 228">
    <line x1="326" y1="0" x2="272" y2="70" stroke="var(--cut)" stroke-width="1.6" stroke-dasharray="6 4"/>
    <circle cx="215" cy="134" r="75" fill="var(--hole)" stroke="var(--cut)" stroke-width="1.6" stroke-dasharray="6 4"/>
  </svg>
  <div class="band back-band">
    <div class="back-brand"><h2 class="brand">VELTA RUG<br>WORKS</h2></div>
    <p class="phone">866-402-5719</p>
    <p class="tagline">WHEN YOU WANT THE BEST FOR LESS<br>CALL VELTA RUG WORKS</p>
  </div>
  <div class="menu">
    <div class="menu-head" style="height:52px">CARPET CLEANING</div>
    <div class="menu-price" style="height:80px">
      <div class="amount"><sup>$</sup>20<span class="small"> OFF</span></div>
      <div class="terms"><b>Coupon</b>Carpet Cleaning<br>Restrictions Apply</div>
    </div>
    <div class="menu-head" style="height:52px">ROOMS<small>STARTING AT</small></div>
    <div class="menu-price" style="height:80px">
      <div class="amount"><sup>$</sup>59<span class="small">.99</span></div>
      <div class="terms"><b>Per Room</b>Deep Steam Clean<br>Restrictions Apply</div>
    </div>
    <div class="menu-head" style="height:40px;font-size:22px">WHY CHOOSE US</div>
    <ul class="perks">
      <li><svg width="10" height="10" viewBox="0 0 10 10"><path d="M1 5l3 3 5-7" fill="none" stroke="var(--blue-deep)" stroke-width="2"/></svg>Carpet, hardwood, tile &amp; grout steam cleaning</li>
      <li><svg width="10" height="10" viewBox="0 0 10 10"><path d="M1 5l3 3 5-7" fill="none" stroke="var(--blue-deep)" stroke-width="2"/></svg>Kid &amp; pet safe</li>
      <li><svg width="10" height="10" viewBox="0 0 10 10"><path d="M1 5l3 3 5-7" fill="none" stroke="var(--blue-deep)" stroke-width="2"/></svg>Fast drying</li>
      <li><svg width="10" height="10" viewBox="0 0 10 10"><path d="M1 5l3 3 5-7" fill="none" stroke="var(--blue-deep)" stroke-width="2"/></svg>100% eco friendly / toxin free products</li>
      <li><svg width="10" height="10" viewBox="0 0 10 10"><path d="M1 5l3 3 5-7" fill="none" stroke="var(--blue-deep)" stroke-width="2"/></svg>Pet stain &amp; odor control</li>
      <li><svg width="10" height="10" viewBox="0 0 10 10"><path d="M1 5l3 3 5-7" fill="none" stroke="var(--blue-deep)" stroke-width="2"/></svg>Same day appointments</li>
      <li><svg width="10" height="10" viewBox="0 0 10 10"><path d="M1 5l3 3 5-7" fill="none" stroke="var(--blue-deep)" stroke-width="2"/></svg>Clean uniformed employees</li>
    </ul>
  </div>
</section>

</body>
</html>
```